Social Media Tool / Marketing Tool homepage design

We need a design template for a website to promote a web based technology / service. The product provide companies with a tools to generate business from social media web site.

We would like a homepage designed and an inner page of the site. This can be a contact us page or a sign up screen... Would also be good to have a design for the blog page of the site and static page i.e affiliates or advertiser page.

The feel of the site should reflect the fact that this is a social media tool but should not be too casual as we will have business clients so a blend between informal, practical and should communicate to business people (professional marketers)

Site should look friendly, thinking rounded edges rather than squared.

We have included logo design and like the idea of using the haxagonal shapes on the background in some way... Also included link to black on black design mock up that's not right as it's too heavy and does not appeal to any of the women we have shown it to. (50% of our audience)

http://mockups.brindlevault-studio.example/ORB/showcase/html/mockup3.html

http://mockups.brindlevault-studio.example/ORB/showcase/html/mockup1_2.html

http://mockups.brindlevault-studio.example/ORB/showcase/html/inner-page1.html

Above link to design that's not right. The taxonomy is right just not the black on black design. We are happy to use black but not black on a black background.

Please consider that we have 4 user types we are trying to sell to on this page hence the 4 blocks on the homepage. Feel free to interparate this how you will could be good as hexagons? or blocks??

Have attached a powerpoint of site pages please take homepage and dummy content and sign up / form page or contact page.

I have also attached logos please only use logo with one coloured hexagon the other file (logo) does not have the hexagon coloured but does include a set of icons that could also be used.

logo font = Metrostyle extended

Target Market(s)

Young professional marketers at bluechip businesses. User of social media sites like pormbly / quillnest and chirvo.

Industry/Entity Type

Business

Requirements
Must have
• should include pormbly, chirvo and quillnest icons (these will link to our profiles on these sites) Should feel friendly yet established, should feel social as this is a tool to market via social media. rounded edges / corners.
Should not have
• not old style fonts not fonts like times roman .. no squared (hard) corners.

```html
<!DOCTYPE html>
<html lang="en">
<head>
<meta charset="utf-8">
<title>Vantora — Advocacy Marketing Platform</title>
<link rel="stylesheet" href="https://fonts.googleapis.com/css2?family=Bebas+Neue&family=Montserrat:wght@400;500;600&family=Arimo:wght@400;700&display=swap">
<style>
:root{
  --orange:#f0571c;
  --orange-light:#ff7a3a;
  --orange-dark:#c8420f;
  --black:#000;
  --ink:#111;
  --panel:#2a2a2a;
  --field:#6b6b6b;
  --grey-text:#555;
  --rule:#c4c4c4;
  --white:#fff;
}
*{box-sizing:border-box;margin:0;padding:0}
html,body{width:1200px;height:768px;overflow:hidden;background:var(--white)}
body{position:relative;font-family:Arimo,Arial,sans-serif;color:var(--ink)}
.abs{position:absolute}

.topbar{left:0;top:0;width:1200px;height:58px;background:var(--black)}
.brand-tile{left:131px;top:0;width:89px;height:87px;background:linear-gradient(#2c2c2c,#000);border-radius:0 0 10px 10px;box-shadow:0 3px 6px rgba(0,0,0,.35);display:flex;align-items:center;justify-content:center}
.brand-tile .dot{width:44px;height:44px;border-radius:50%;background:var(--orange)}
.brand-name{left:238px;top:14px;font-family:Montserrat,sans-serif;font-weight:600;font-size:24px;color:var(--white);letter-spacing:.5px}
.login-panel{left:633px;top:10px;width:360px;height:38px;background:var(--panel);border-radius:4px 0 0 4px}
.login-field{top:19px;height:23px;background:var(--field);border-radius:5px;border:1px solid #888;color:#aaa;font-size:11px;line-height:21px;padding-left:9px}
.login-field.member{left:670px;width:153px}
.login-field.pass{left:833px;width:153px}
.login-btn{left:1002px;top:17px;font-family:"Bebas Neue",sans-serif;font-size:22px;color:var(--orange);letter-spacing:.5px}

.hex-backdrop{left:30px;top:58px;width:340px;height:230px;background:radial-gradient(circle at 30% 30%,rgba(236,236,236,.9),rgba(255,255,255,0) 70%)}
.hero-mark{left:202px;top:108px;width:103px;height:118px;border-radius:18px;background:linear-gradient(135deg,#fff 0%,#fde6dc 100%);border:3px solid rgba(240,87,28,.25)}

.main-nav{left:503px;top:55px;height:43px;display:flex;font-family:"Bebas Neue",sans-serif;font-size:20px;color:#333;letter-spacing:.4px}
.main-nav a{color:inherit;text-decoration:none;padding:15px 0 0;margin-right:23px}
.main-nav a.current{background:linear-gradient(#3a3a3a,#000);color:var(--white);border-radius:0 0 7px 7px;padding:15px 13px 0;margin-right:12px}

.hero-kicker{left:330px;top:135px;font-family:"Bebas Neue",sans-serif;font-size:28px;color:var(--orange)}
.hero-title{left:326px;top:156px;font-family:"Bebas Neue",sans-serif;font-size:48px;color:var(--black);letter-spacing:0;font-weight:400}
.hero-copy{left:326px;top:209px;width:520px;font-size:17px;line-height:24px;color:var(--grey-text)}
.hero-copy em{color:var(--orange)}
.subscribe{left:867px;top:152px;width:204px;height:46px;border-radius:6px;background:linear-gradient(var(--orange-light),var(--orange-dark));font-family:"Bebas Neue",sans-serif;font-size:23px;line-height:19px;color:var(--white);padding:5px 0 0 22px;letter-spacing:.5px;overflow:hidden}

.audience-card{top:279px;width:234px;height:182px;border-radius:6px;background:linear-gradient(#3a3a3a 0,#151515 55px,#000 100%);box-shadow:0 2px 4px rgba(0,0,0,.4)}
.audience-card .icon-box{position:absolute;left:0;top:0;width:66px;height:54px;background:#000;border-radius:6px 0 8px 0;display:flex;align-items:center;justify-content:center}
.audience-card h2{position:absolute;left:78px;top:17px;font-family:Montserrat,sans-serif;font-weight:500;font-size:18px;color:var(--white);letter-spacing:1px}
.audience-card ul{position:absolute;left:16px;top:68px;width:200px;list-style:none;color:var(--white);font-size:13px;line-height:13px}
.audience-card li{margin-bottom:12px}
.register{top:443px;width:150px;height:34px;border-radius:4px;background:linear-gradient(var(--orange-light),var(--orange-dark));font-family:"Bebas Neue",sans-serif;font-size:22px;color:var(--white);padding:6px 0 0 16px;letter-spacing:.5px;box-shadow:0 2px 3px rgba(0,0,0,.3)}
.register::after,.subscribe::after{content:"";position:absolute;right:14px;top:50%;width:14px;height:14px;border-top:5px solid #fff;border-right:5px solid #fff;transform:translateY(-50%) rotate(45deg);opacity:.9}

.lead-heading{left:0;top:503px;width:1200px;text-align:center;font-family:Montserrat,sans-serif;font-size:17px;color:var(--black);font-weight:400}
.lead-heading span{color:var(--orange);font-size:23px;font-weight:500}
.benefit{top:555px;width:192px;font-size:13px;line-height:18px;color:#222;padding-left:26px}
.benefit::before{content:"";position:absolute;left:2px;top:7px;width:7px;height:7px;border-top:3px solid var(--orange);border-right:3px solid var(--orange);transform:rotate(45deg)}

.social-rule{left:0;top:645px;width:1200px;height:5px;background:var(--rule)}
.get-social{left:570px;top:626px}
.get-social span{position:absolute;left:0;top:16px;width:60px;text-align:center;font-family:"Bebas Neue",sans-serif;font-size:17px;line-height:17px;color:var(--orange)}
.social-name{top:668px;font-family:Montserrat,sans-serif;font-weight:600;font-size:19px;color:#555}

.footer{left:0;top:711px;width:1200px;height:57px;background:var(--black);color:var(--white);font-size:12px}
.footer nav{position:absolute;left:147px;top:14px;display:flex;gap:20px}
.footer small{position:absolute;left:816px;top:16px;font-size:12px}
</style>
</head>
<body>
<header>
  <div class="abs topbar"></div>
  <div class="abs brand-tile"><span class="dot"></span></div>
  <div class="abs brand-name">Vantora</div>
  <div class="abs login-panel"></div>
  <div class="abs login-field member">Member Login</div>
  <div class="abs login-field pass">Password</div>
  <div class="abs login-btn">Login ›</div>
  <nav class="abs main-nav">
    <a class="current" href="#">Home</a><a href="#">What?</a><a href="#">Why?</a><a href="#">Demo</a><a href="#">Reports</a><a href="#">Blog</a><a href="#">Pricing</a><a href="#">Contact Us</a>
  </nav>
</header>

<div class="abs hex-backdrop" role="img" aria-label="Faint hexagon background pattern"></div>
<div class="abs hero-mark" role="img" aria-label="Orange hexagon emblem with small hexagon cluster"></div>

<section>
  <div class="abs hero-kicker">Demand Generation &amp; Social Engagement</div>
  <h1 class="abs hero-title">Advocacy Marketing Platform</h1>
  <p class="abs hero-copy">Our platform allows advertisers to easily create <em>surveys and lead generation campaigns</em> and publish them across the social web.</p>
  <div class="abs subscribe">Subscribe to<br>our newsletter</div>
</section>

<section>
  <article class="abs audience-card" style="left:127px">
    <div class="icon-box"><svg width="24" height="34" viewBox="0 0 24 34" fill="none" stroke="#fff" stroke-width="2.5"><rect x="7" y="1" width="10" height="19" rx="5" fill="#fff"/><path d="M3 14a9 9 0 0 0 18 0M12 23v9M6 32h12"/></svg></div>
    <h2>ADVERTISERS</h2>
    <ul><li>Create Polls and surveys</li><li>Create Competitions</li><li>Create B2B and B2C demand generation campaigns</li></ul>
  </article>
  <article class="abs audience-card" style="left:366px">
    <div class="icon-box"><svg width="34" height="34" viewBox="0 0 34 34" stroke="#fff" stroke-width="2.5" fill="#fff"><path d="M17 17V5M17 17L6 24M17 17l11 7"/><circle cx="17" cy="17" r="4"/><circle cx="17" cy="5" r="3.5"/><circle cx="6" cy="24" r="3.5"/><circle cx="28" cy="24" r="3.5"/></svg></div>
    <h2>AFFILIATES</h2>
    <ul><li>10% revenue share for tier one referrals</li><li>5% revenue share for second tier referrals</li><li>Real time reporting</li></ul>
  </article>
  <article class="abs audience-card" style="left:604px">
    <div class="icon-box"><svg width="24" height="34" viewBox="0 0 24 34"><path d="M16 1L3 19h8l-4 14 14-19h-8z" fill="#fff"/></svg></div>
    <h2>ADVOCATES</h2>
    <ul><li>Choose from both D2C or B2B campaigns</li><li>Paid per lead</li><li>Full marketing tool kit</li></ul>
  </article>
  <article class="abs audience-card" style="left:841px">
    <div class="icon-box"><svg width="34" height="28" viewBox="0 0 34 28"><path d="M12 6V2h10v4" fill="none" stroke="#fff" stroke-width="2.5"/><rect x="1" y="6" width="32" height="21" rx="2" fill="#fff"/></svg></div>
    <h2>AGENCIES</h2>
    <ul><li>White label solution, upload logo or update CSS for full brand control</li><li>Build web forms to capture data</li><li>Dealforge extension</li></ul>
  </article>
  <div class="abs register" style="left:165px">Register</div>
  <div class="abs register" style="left:404px">Register</div>
  <div class="abs register" style="left:641px">Register</div>
  <div class="abs register" style="left:879px">Register</div>
</section>

<section>
  <h3 class="abs lead-heading">Generate Lead via <span>Social Media Email and Our Publisher Network...</span></h3>
  <p class="abs benefit" style="left:142px">Create branded campaign landing pages without IT or any technical skills</p>
  <p class="abs benefit" style="left:381px">Engage with your audience on the social web, survey them for insights</p>
  <p class="abs benefit" style="left:622px">Generate leads from quillnest, chirvo and pormbly.</p>
  <p class="abs benefit" style="left:860px">Reduce your sales cycle by providing your</p>
</section>

<section>
  <div class="abs social-rule"></div>
  <div class="abs get-social">
    <svg width="60" height="68" viewBox="0 0 60 68"><polygon points="30,2 58,18 58,50 30,66 2,50 2,18" fill="#fff" stroke="#c4c4c4" stroke-width="4" stroke-linejoin="round"/></svg>
    <span>Get<br>Social</span>
  </div>
  <div class="abs social-name" style="left:309px">quillnest</div>
  <div class="abs social-name" style="left:456px">chirvo</div>
  <div class="abs social-name" style="left:669px">Tumbleway</div>
  <div class="abs social-name" style="left:817px">pormbly</div>
</section>

<footer class="abs footer">
  <nav><span>About Us</span><span>Contact Us</span><span>Sitemap</span><span>Privacy Policy</span></nav>
  <small>Copyright 2011 Vantora.example. All rights reserved.</small>
</footer>
</body>
</html>
```